Solvanta Clinica Business Card Design and print

I have attached the design I require including JPEG for company logo. I would like a copy of the art work for future needs.

Double sided - the item will not change from single

250 cards with both names on Ruth Calloway and Megan Thorpe

250 cards with Ruth Calloway only

Industry/Entity Type

Business

Contact Information for Business Card

See attached layout

```html
<!DOCTYPE html>
<html lang="en">
<head>
<meta charset="utf-8">
<title>Solvanta Clinica – Business Card</title>
<link rel="stylesheet" href="https://fonts.googleapis.com/css2?family=Questrial&display=swap">
<style>
  :root {
    --stage: #e9e6e1;
    --card-dark: #262626;
    --card-light: #ffffff;
    --orange: #e8822a;
    --purple: #7b4fa3;
    --shadow: rgba(0, 0, 0, 0.22);
  }
  * { box-sizing: border-box; margin: 0; padding: 0; }
  html, body {
    width: 1200px;
    height: 1000px;
    overflow: hidden;
    background: var(--stage);
    font-family: "Questrial", "Century Gothic", sans-serif;
  }
  .stage {
    width: 1200px;
    height: 1000px;
    display: flex;
    flex-direction: column;
    align-items: center;
    justify-content: center;
    gap: 60px;
  }
  .card {
    width: 700px;
    height: 400px;
    position: relative;
    box-shadow: 0 12px 30px var(--shadow);
  }
  .card--back { background: var(--card-dark); }
  .card--front { background: var(--card-light); }

  .wordmark {
    display: flex;
    align-items: center;
    gap: 22px;
    color: var(--orange);
    font-size: 64px;
    letter-spacing: 1px;
    line-height: 1;
  }
  .wordmark__square {
    width: 70px;
    height: 70px;
    background: var(--purple);
    flex: none;
  }
  .card--back .wordmark {
    position: absolute;
    left: 50%;
    top: 50%;
    transform: translate(-50%, -50%);
    white-space: nowrap;
  }

  .card--front .wordmark {
    position: absolute;
    right: 48px;
    top: 56px;
    font-size: 46px;
    gap: 16px;
  }
  .card--front .wordmark__square { width: 52px; height: 52px; }

  .contact {
    position: absolute;
    left: 48px;
    top: 200px;
  }
  .contact__name {
    color: var(--purple);
    font-size: 30px;
    margin-bottom: 10px;
  }
  .contact__line {
    color: var(--orange);
    font-size: 18px;
    line-height: 1.55;
  }
  .website {
    position: absolute;
    left: 48px;
    bottom: 36px;
    color: var(--purple);
    font-size: 17px;
  }
  .corner-mark {
    position: absolute;
    right: 48px;
    bottom: 32px;
    width: 44px;
    height: 44px;
    background: var(--purple);
  }
</style>
</head>
<body>
  <main class="stage">
    <section class="card card--back" aria-label="Card back">
      <div class="wordmark">
        <span class="wordmark__square"></span>
        <span class="wordmark__name">solvanta clinica</span>
      </div>
    </section>

    <section class="card card--front" aria-label="Card front">
      <div class="wordmark">
        <span class="wordmark__square"></span>
        <span class="wordmark__name">solvanta clinica</span>
      </div>
      <div class="contact">
        <p class="contact__name">Ruth Calloway</p>
        <p class="contact__line">P: +61 (0)400 555 018</p>
        <p class="contact__line">E: ruth@solvantaclinica.com</p>
      </div>
      <p class="website">www.solvantaclinica.com.au</p>
      <span class="corner-mark"></span>
    </section>
  </main>
</body>
</html>
```